Corporate Business Card

Very professional, Modern, Not to busy, include phone address email, website
(253) 555-0174, 61807 19th Street N, Kent, WA 98517, marcus@kestrelbayholding.com, brelvanindustries.com

Target Market(s)

Manufacturing

Industry/Entity Type

Aero, machining, manufacturing, Off road racing

Contact Information for Business Card

Phone, address email, website

```html
<!DOCTYPE html>
<html lang="en">
<head>
<meta charset="utf-8">
<title>Brelvan Industries — Business Card</title>
<link href="https://fonts.googleapis.com/css2?family=Carlito:wght@400;700&display=swap" rel="stylesheet">
<style>
  :root {
    --backdrop: #adadad;
    --card-white: #ffffff;
    --navy: #16356e;
    --navy-deep: #1b3a78;
    --navy-muted: #243f78;
    --accent-red: #d42a2a;
    --text-dark: #2e2e2e;
    --text-mid: #555555;
    --rule: #9a9a9a;
  }
  * { margin: 0; padding: 0; box-sizing: border-box; }
  html, body {
    width: 1200px; height: 1000px; overflow: hidden;
    background: var(--backdrop);
    font-family: "Carlito", "Calibri", sans-serif;
  }
  .card {
    position: absolute; left: 294px; width: 613px; height: 352px;
    border-radius: 24px;
  }
  .card-front { top: 111px; background: var(--card-white); }
  .card-back { top: 517px; background: var(--navy); }

  .wordmark {
    position: absolute; display: flex; align-items: center; gap: 8px;
    font-weight: 700; font-size: 25px; color: var(--navy-deep);
    white-space: nowrap;
  }
  .wordmark-mark { width: 11px; height: 11px; background: var(--accent-red); }
  .card-front .wordmark { left: 66px; top: 162px; }
  .card-back .wordmark { left: 50%; top: 50%; transform: translate(-50%, -50%); color: var(--navy-muted); }
  .card-back .wordmark-mark { background: #7a2a45; }

  .divider-vertical {
    position: absolute; left: 306px; top: 127px; width: 1px; height: 98px;
    background: var(--rule);
  }
  .contact-list {
    position: absolute; left: 333px; top: 141px; list-style: none;
    font-size: 16.5px; color: var(--text-dark); line-height: 21.5px;
  }
  .contact-list li { display: flex; align-items: center; gap: 5px; }
  .contact-list svg { width: 10px; height: 10px; fill: var(--accent-red); flex: none; }

  .divider-horizontal {
    position: absolute; left: 49px; right: 49px; top: 298px; height: 1px;
    background: var(--rule);
  }
  .address {
    position: absolute; left: 0; right: 0; top: 315px;
    display: flex; justify-content: center; align-items: center; gap: 6px;
    font-size: 16.5px; color: var(--text-mid);
  }
  .address svg { width: 9px; height: 12px; fill: var(--accent-red); }
</style>
</head>
<body>
  <section class="card card-front">
    <div class="wordmark"><span class="wordmark-mark"></span>Brelvan Industries</div>
    <div class="divider-vertical"></div>
    <ul class="contact-list">
      <li>
        <svg viewBox="0 0 10 10" aria-hidden="true"><path d="M3 0h4a1 1 0 0 1 1 1v8a1 1 0 0 1-1 1H3a1 1 0 0 1-1-1V1a1 1 0 0 1 1-1zm0 1.5v6h4v-6zM5 8.2a.5.5 0 1 0 0 1 .5.5 0 0 0 0-1z"/></svg>
        (253) 555-0174
      </li>
      <li>
        <svg viewBox="0 0 10 10" aria-hidden="true"><path d="M0 2h10v6H0zM.8 2.6 5 5.6l4.2-3v.9L5 6.5.8 3.5z" fill-rule="evenodd"/></svg>
        marcus@kestrelbayholding.com
      </li>
      <li>
        <svg viewBox="0 0 10 10" aria-hidden="true"><path d="M5 .5a4.5 4.5 0 1 0 0 9 4.5 4.5 0 0 0 0-9zm0 1c.6.6 1 1.6 1.1 2.9H3.9C4 3.1 4.4 2.1 5 1.5zM1.6 4.4h1.3c.1 1.2.4 2.3.9 3A3.5 3.5 0 0 1 1.6 4.4zm0 1.2zM3.9 5.6h2.2C6 6.9 5.6 7.9 5 8.5 4.4 7.9 4 6.9 3.9 5.6zm3.2-1.2c-.1-1.2-.4-2.3-.9-3a3.5 3.5 0 0 1 2.2 3z"/></svg>
        brelvanindustries.com
      </li>
    </ul>
    <div class="divider-horizontal"></div>
    <p class="address">
      <svg viewBox="0 0 9 12" aria-hidden="true"><path d="M4.5 0A4.5 4.5 0 0 0 0 4.5C0 8 4.5 12 4.5 12S9 8 9 4.5A4.5 4.5 0 0 0 4.5 0zm0 6.2a1.7 1.7 0 1 1 0-3.4 1.7 1.7 0 0 1 0 3.4z"/></svg>
      61807 19th Street N, Kent, WA 98517
    </p>
  </section>

  <section class="card card-back">
    <div class="wordmark"><span class="wordmark-mark"></span>Brelvan Industries</div>
  </section>
</body>
</html>
```